Brochure Design- Targeted at Property Developers

We are the largest Conveyancing (property law) firm in the state of Victoria, Australia.

We need a very sophisticated brochure to enable us to take the next step and compete with law firms for property developer clients.

Much about us can be found on our website (inlcuding logos, photos, etc) www.brindlecove.com.au but our business name is Brindlecove- Marlow Reach not just Brindlecove. ALSO I HAVE ATTACHED MANY PHOTOS OF OUR STAFF AND SOME LOGOS TO HELP!!

Size: fold (A3 double sided so that there is 4 A4 pages)

Copy:

This can be played with by the designer to spread across the 4 pages. Ideally the front page will be very minimalistic and not mention our brand (or at least the brand should not dominate):

Page 1: Do property developers have a genuine alternative to high legal fees?

Page 2 and 3:

- 100% of our developer clients recommend us
- We already look after the Conveyancing needs of more developers in Victoria than any other Conveyancing firm
- Industry benchmark off- the- plan contracts (tailored to the requirements of each development). Our special conditions (including variations, rebates and resale restrictions) are carefully chosen to protect the interests of our vendors while being commercially sensitive to ensure sales are not lost unnecessarily
- Expert in guiding developers from first time dual occupancies to seasoned developers of large scale land and highrise projects
- Our large team and highly refined systems ensure fastest possible settlement times after subdivision registration
- We are available to train your project marketers on completing and executing contracts so that sales are not delayed or lost
- Establishment of interest bearing trust accounts
- Before you buy a development site have us thoroughly investigate the contract and vendors statement. We can then conduct the purchase settlement on your behalf.
- We have the friendliest and most efficient staff. Every dealing you have with our dedicated Development Division will be prompt, professional and impressive. You will never need to follow us up!
- Highly experienced Conveyancers with the security of full Solicitor support

Please consider us next time you need Conveyancing.

Services options:
- Use us from contract preparation to settlement or;
- Have your Solicitor prepare the contract and use us as an alternative for the settlement stage only. Many Solicitors recommend us for this service already
- Fast subdivision lodgements (including obtaining mortgagee’s consent, Solicitor preparation of Land Titles Office application, owners corporation establishment)

Page 4: Just our contact details (see our website)

The design should make us look highly professional, conservative, yet cutting edge.
Updates

Target Market(s)

Property developers of small to medium sized land and unit developments

Industry/Entity Type

Security

Requirements
Must have
• - Our logo and contact details as well as the copy above.
Nice to have
• - Pictures of land sites, highrise buildings under construction
Should not have
• I really dislike overly corny photos where everyone is fake and smiling. Other photos would be great but not too cheesy.

```html
<!DOCTYPE html>
<html lang="en">
<head>
<meta charset="utf-8">
<title>Brindlecove- Marlow Reach — Developer Brochure Cover</title>
<link rel="stylesheet" href="https://fonts.googleapis.com/css2?family=EB+Garamond:wght@400&family=Fira+Sans:wght@700&display=swap">
<style>
  :root {
    --navy: #003a56;
    --rust: #c0631f;
    --ink: #3a3a38;
    --white: #ffffff;
    --photo-light: #f1ece0;
    --photo-mid: #c9b894;
    --photo-dark: #5e5340;
  }
  * { margin: 0; padding: 0; box-sizing: border-box; }
  html, body { width: 1200px; height: 847px; overflow: hidden; background: #ffffff; }
  .spread { position: relative; width: 1200px; height: 847px; display: flex; }

  /* Back cover */
  .back-cover { position: relative; width: 600px; height: 847px; background: var(--navy); }
  .contact { position: absolute; left: 58px; top: 440px; color: var(--white); font-family: "EB Garamond", Georgia, serif; }
  .brand-name { display: flex; align-items: flex-start; gap: 5px; font-family: "EB Garamond", Georgia, serif; font-weight: 400; line-height: 1; }
  .brand-name .mark { width: 10px; height: 10px; margin-top: 2px; }
  .contact .brand-name { color: var(--white); font-size: 12.5px; margin: 0 0 32px 4px; }
  .contact .brand-name .mark { background: var(--white); }
  .brand-name .words span { display: block; }
  .brand-name .words span + span { padding-left: 14px; }
  .address { font-size: 9.6px; line-height: 10.7px; }
  .details { border-collapse: collapse; font-size: 9.6px; line-height: 10.7px; }
  .details td { padding: 0; vertical-align: top; }
  .details .label { width: 70px; }
  .details .sep { width: 16px; }

  /* Front cover */
  .front-cover { position: relative; width: 600px; height: 847px; overflow: hidden; }
  .cover-photo {
    position: absolute; inset: 0;
    background:
      linear-gradient(125deg, rgba(255,255,255,0) 40%, rgba(94,83,64,0.35) 100%),
      linear-gradient(160deg, var(--photo-mid) 0%, var(--photo-light) 35%, var(--photo-mid) 60%, var(--photo-dark) 100%);
  }
  .front-cover .brand-name { position: absolute; left: 653px; left: 53px; top: 344px; color: var(--ink); font-size: 14px; }
  .front-cover .brand-name .mark { background: var(--ink); }
  .headline-band {
    position: absolute; left: 0; top: 415px; width: 600px; height: 215px;
    background: var(--rust); opacity: 0.92;
  }
  .headline {
    position: absolute; left: 52px; top: 433px; width: 520px;
    font-family: "Fira Sans", Arial, sans-serif; font-weight: 700;
    font-size: 37px; line-height: 43px; color: var(--white); letter-spacing: -0.2px;
  }
</style>
</head>
<body>
<main class="spread">
  <section class="back-cover">
    <div class="contact">
      <div class="brand-name"><i class="mark"></i><div class="words"><span>Brindlecove</span><span>Marlow Reach</span></div></div>
      <p class="address">Level 7, 18 Harlan Crescent<br>Melbourne 3004 Victoria<br>Australia<br>(Off Linden Road)</p>
      <table class="details">
        <tr><td class="label">Postal</td><td class="sep">:</td><td>PO Box 4120 Linden Road Central Melbourne 8008</td></tr>
        <tr><td class="label">DX Postal</td><td class="sep">:</td><td>DX 41870 South Melbourne</td></tr>
        <tr><td class="label">Phone</td><td class="sep">:</td><td>(03) 9014 2270</td></tr>
        <tr><td class="label">International</td><td class="sep">:</td><td>+61 3 9014 2270</td></tr>
        <tr><td class="label">Fax</td><td class="sep">:</td><td>(03) 9014 2271</td></tr>
        <tr><td class="label">International Fax</td><td class="sep">:</td><td>+61 3 9014 2271</td></tr>
        <tr><td class="label">Email</td><td class="sep">:</td><td>marlowreach@brindlecove.com.au</td></tr>
      </table>
    </div>
  </section>

  <section class="front-cover">
    <div class="cover-photo" role="img" aria-label="Upward view of a glass and steel high-rise facade with criss-crossing structural lines in warm sand tones"></div>
    <div class="brand-name"><i class="mark"></i><div class="words"><span>Brindlecove</span><span>Marlow Reach</span></div></div>
    <div class="headline-band"></div>
    <h1 class="headline">Do property developers have a genuine alternative to high legal fees?</h1>
  </section>
</main>
</body>
</html>
```